Velqora new official website

We need a new design for our website www.velqora-example.com We are web marketing publishers and our website must be attractive for clients. That's why we need to "refresh" it. The main colour of our logo is orange, and this is an indication for the colours of the website too. We need the design for the homepage and the design of inner pages. Here is the list of the various sections of the website:
- ABOUT US: Who we are/Certificates/Offices/Team
- SERVICES: SEM/Display/Email Marketing and coregistration/ad networking
- PROJECTS/NETWORK/BRANDS: We need one page per country with screenshots of the websites and very short descriptions.
- VELQORA & CHARITY
- WORK WITH US
- CONTACT US
- NEWS

```html
<!DOCTYPE html>
<html lang="en">
<head>
<meta charset="utf-8">
<title>Velqora — Home</title>
<link href="https://fonts.googleapis.com/css2?family=Open+Sans:wght@300;400;600;700;800&display=swap" rel="stylesheet">
<style>
:root{
  --orange:#f47a20;
  --orange-dark:#d85f0c;
  --orange-soft:#fbb36d;
  --ink:#333333;
  --muted:#6b6b6b;
  --line:#d9d9d9;
  --panel:#f2f2f2;
  --nav:#5a5a5a;
  --white:#ffffff;
}
*{box-sizing:border-box;margin:0;padding:0}
html,body{width:880px;height:1200px;overflow:hidden;background:var(--white)}
body{font-family:"Open Sans",Arial,sans-serif;color:var(--ink);font-size:10px;position:relative}
.page{position:relative;width:880px;height:1200px}
a{color:inherit;text-decoration:none}

/* header */
.brand{position:absolute;left:22px;top:14px;display:flex;align-items:center;gap:8px}
.brand-name{font-size:30px;font-weight:700;color:var(--orange);letter-spacing:-.5px}
.brand-dot{width:30px;height:30px;border-radius:50%;background:var(--nav)}
.search{position:absolute;right:20px;top:22px;display:flex}
.search-field{width:150px;height:22px;border:1px solid var(--line);border-radius:3px 0 0 3px;background:var(--white)}
.search-btn{height:22px;padding:0 12px;background:var(--ink);color:var(--white);font-size:9px;font-weight:700;line-height:22px;border-radius:0 3px 3px 0}

/* nav */
.main-nav{position:absolute;left:12px;top:64px;width:856px;height:28px;border-radius:6px;background:linear-gradient(#efefef,#d8d8d8);display:flex;overflow:hidden;border:1px solid #cfcfcf}
.main-nav a{flex:none;padding:0 26px;line-height:26px;font-size:11px;font-weight:600;color:var(--ink);border-right:1px solid #c6c6c6}
.main-nav a.active{background:linear-gradient(var(--orange-soft),var(--orange));color:var(--white)}

/* hero */
.hero-visual{position:absolute;left:14px;top:98px;width:420px;height:234px;border-radius:4px;background:radial-gradient(ellipse at 40% 50%,#5a5a5a,#1d1d1d 75%)}
.hero-title{position:absolute;left:450px;top:102px;width:410px;text-align:center}
.hero-title .lead{display:block;font-size:30px;font-weight:300;color:var(--muted);line-height:36px}
.hero-title .lead b{font-weight:700;color:var(--ink)}
.hero-title .big{display:block;font-size:46px;font-weight:800;color:var(--orange);line-height:50px}
.promo{position:absolute;top:198px;width:198px;height:134px;border-radius:6px;padding:10px 12px 30px}
.promo h3{font-size:12px;font-weight:700;text-align:center;margin-bottom:6px;line-height:1.35}
.promo p{font-size:7.5px;line-height:1.5}
.promo .more{position:absolute;right:10px;bottom:8px;font-size:8px;padding:2px 10px;border-radius:3px}
.promo-mission{left:452px;background:linear-gradient(var(--orange-soft),var(--orange));color:var(--white)}
.promo-mission .more{background:var(--orange-dark)}
.promo-clients{left:660px;background:linear-gradient(#8c8c8c,#555);color:var(--white)}
.promo-clients h3{color:var(--orange-soft)}
.promo-clients .more{background:var(--ink)}

/* section headings */
.heading{position:absolute;display:flex;align-items:center;gap:6px}
.heading .icon{width:34px;height:34px;border-radius:50%;border:3px solid var(--orange);background:var(--panel)}
.heading h2{font-size:20px;font-weight:300;color:var(--muted)}
.heading h2 b{font-weight:800;color:var(--orange)}

/* expertise */
.expertise{position:absolute;left:22px;top:420px;width:290px}
.exp-item{position:relative;padding:4px 0 6px 12px;border-bottom:1px dotted var(--line);height:52px}
.exp-item::before{content:"";position:absolute;left:0;top:8px;width:6px;height:6px;border-radius:50%;background:var(--orange)}
.exp-item h4{font-size:9px;color:var(--orange);font-weight:700}
.exp-item p{font-size:7px;color:var(--muted);line-height:1.45}
.exp-item .more{position:absolute;right:0;bottom:4px;font-size:7px;color:var(--orange);text-decoration:underline}

/* partners */
.partners{position:absolute;left:340px;top:418px;width:520px;height:64px;border:1px solid var(--line);border-radius:4px;display:flex;align-items:center;justify-content:space-around;padding:0 20px;background:linear-gradient(#fff,#f5f5f5)}
.partner{width:62px;height:36px;border-radius:4px;background:#e4e4e4}
.partner.warm{background:var(--orange-soft)}
.sites{position:absolute;left:340px;top:572px;width:520px;height:108px;border-radius:4px;background:linear-gradient(90deg,#d9d9d9,#f4f4f4 50%,#d9d9d9)}
.arrow{position:absolute;top:616px;width:16px;height:20px}

/* bottom */
.contact{position:absolute;left:22px;top:740px;width:260px;font-size:7.5px;line-height:1.55;color:var(--muted)}
.contact p{margin-bottom:8px}
.contact b{color:var(--ink)}
.news-img{position:absolute;left:320px;top:742px;width:250px;height:148px;border-radius:3px;background:linear-gradient(#7a7a7a,#2f2f2f)}
.news-cap{position:absolute;left:320px;top:896px;width:250px;font-size:7.5px;color:var(--ink)}
.news-list{position:absolute;left:600px;top:742px;width:260px}
.news-list li{list-style:none;position:relative;padding:0 0 10px 10px;font-size:7.5px;line-height:1.5;color:var(--muted)}
.news-list li::before{content:"";position:absolute;left:0;top:4px;width:5px;height:5px;background:var(--orange)}
.news-list a{color:var(--orange);text-decoration:underline}

/* footer */
.footer{position:absolute;left:0;top:1118px;width:880px;height:82px;background:var(--panel);border-top:3px solid var(--orange);text-align:center;padding-top:14px}
.footer nav{font-size:8px;color:var(--ink)}
.footer nav a{margin:0 6px}
.footer small{display:block;margin-top:8px;font-size:7px;color:var(--muted)}
</style>
</head>
<body>
<div class="page">
  <header>
    <div class="brand"><span class="brand-name">Velqora</span><span class="brand-dot"></span></div>
    <div class="search"><span class="search-field"></span><span class="search-btn">SEARCH</span></div>
  </header>

  <nav class="main-nav">
    <a class="active" href="#">Home</a>
    <a href="#">About Us</a>
    <a href="#">Services</a>
    <a href="#">Projects/ Network/ Brands</a>
    <a href="#">Velqora</a>
    <a href="#">Work with Us</a>
    <a href="#">Email</a>
  </nav>

  <section>
    <div class="hero-visual" role="img" aria-label="Collage of website screens on dark background with orange light effects"></div>
    <div class="hero-title">
      <span class="lead">The <b>MAIN WAY</b> to Your</span>
      <span class="big">BUSINESS</span>
    </div>
    <div class="promo promo-mission">
      <h3>Scope and Mission</h3>
      <p>Our aim is creating strong value for our customers, both through technology and web marketing by means of the most modern and advertising systems, the best for customers in developing new markets.</p>
      <a class="more" href="#">Read more</a>
    </div>
    <div class="promo promo-clients">
      <h3>Clients' strategies &amp; web know-how</h3>
      <p>We cooperate with the most international brands in the field of tourism, finance, fashion, retail and technology, offering communication solutions that support our partners in finding the best audience.</p>
      <a class="more" href="#">Read more</a>
    </div>
  </section>

  <div class="heading" style="left:22px;top:376px"><span class="icon"></span><h2>Field of <b>EXPERTISE</b></h2></div>
  <div class="expertise">
    <div class="exp-item"><h4>Desktop</h4><p>Search engines and display campaigns planned for the best national and international web results.</p><a class="more" href="#">Read more</a></div>
    <div class="exp-item"><h4>Technologies &amp; Communication</h4><p>Our technical team builds tools and platforms that bring every campaign closer to its audience.</p><a class="more" href="#">Read more</a></div>
    <div class="exp-item"><h4>Analysis</h4><p>Data and traffic studies guide each project from planning through to final reporting.</p><a class="more" href="#">Read more</a></div>
    <div class="exp-item"><h4>Career</h4><p>We look for new talents in marketing, development and design to join our offices.</p><a class="more" href="#">Read more</a></div>
    <div class="exp-item"><h4>Double Sector</h4><p>Publishing and advertising together create stronger value for clients and partners.</p><a class="more" href="#">Read more</a></div>
  </div>

  <div class="partners">
    <span class="partner"></span><span class="partner warm"></span><span class="partner"></span><span class="partner warm"></span><span class="partner"></span>
  </div>

  <div class="heading" style="left:340px;top:526px"><span class="icon"></span><h2>Our <b>SITES/ BRANDS</b></h2></div>
  <svg class="arrow" style="left:344px" viewBox="0 0 16 20"><path d="M12 2 L4 10 L12 18" fill="none" stroke="#f47a20" stroke-width="3"/></svg>
  <div class="sites" role="img" aria-label="Row of website screenshots from the network brands" style="left:364px;width:472px"></div>
  <svg class="arrow" style="left:842px" viewBox="0 0 16 20"><path d="M4 2 L12 10 L4 18" fill="none" stroke="#f47a20" stroke-width="3"/></svg>

  <div class="heading" style="left:22px;top:696px"><span class="icon"></span><h2>Contact <b>Us</b></h2></div>
  <div class="contact">
    <p><b>HEAD OFFICE:</b> Velqora srl, Via Nuova Porta 8, 00154 Castelvia, Italy<br>Tel. +39 000 000 0000 — Fax +39 000 000 0001</p>
    <p><b>BRANCH OFFICE:</b> Via dei Giardini 12, 20121 Castelvia<br>Tel. +39 000 000 0002</p>
    <p><b>BRANCH OFFICE:</b> Calle Mayor 21, 08002 Portalmar, Spain<br>Tel. +34 000 000 000</p>
    <p>info@velqora-example.com<br>www.velqora-example.com</p>
  </div>

  <div class="heading" style="left:320px;top:696px"><span class="icon"></span><h2>Velqora <b>NEWS</b></h2></div>
  <div class="news-img" role="img" aria-label="News photo of a city skyline at dusk"></div>
  <p class="news-cap"><b>January 2013:</b> Opening of new branches in Spain... <a href="#" style="color:var(--orange)">[read more]</a></p>

  <div class="heading" style="left:600px;top:696px"><span class="icon"></span><h2>Nexlio <b>NEWS</b></h2></div>
  <ul class="news-list">
    <li>Social Design Strategy: thinking from the outside to inside is a shift that lets every brand speak with its audience. <a href="#">read more</a></li>
    <li>Newsletter best practices: simple rules to improve open rates and keep readers engaged over time. <a href="#">read more</a></li>
    <li>Seven Big Gen Ideas for the future of display networks and new publishing formats. <a href="#">read more</a></li>
  </ul>

  <footer class="footer">
    <nav><a href="#">Home</a>|<a href="#">About Us</a>|<a href="#">Services</a>|<a href="#">Projects/ Network/ Brands</a>|<a href="#">Velqora</a>|<a href="#">Work with Us</a>|<a href="#">Email</a></nav>
    <small>VELQORA srl, Via Nuova Porta 8, 00154 Castelvia — Tel. +39 000 000 0000 — P.IVA 00000000000<br>© All rights reserved — www.velqora-example.com</small>
  </footer>
</div>
</body>
</html>
```